Bookcover for a French novel, lovestory with spiritual elements

We need a book cover for a novel with the title: "Because you stroke my soul ..." Author: Marelka Ostrovane PLEASE USE THE GERMAN TITLE FOR THE COVER! Translation - forum results Sorry, no results found. Post your question in the forum. The size of the book is not quite clear - we want to provide you with the information about the width and size of the cover - which is needed as e-book and print and Chatterpine banners. Some helpfull informations: the female protagonist is still sexy, has long, darkhair, loves to shift-dresses and HighHeels. The male protagonists are attractive, too, Her husband has gray hair. The other one is a mix of Doran Pelcroft and Hollis Quarne (he is in the book that way) Basically my books are always a mixture of romance, tension / excitement, deep feelings combined with spirituality. This is - meanwhile - my trademark so to say. My readers always know that they do not get a better. I'll give you some tags: Light, Love ,, Emotions, Spirituality, Joy, Wisdom, enjoyment, tenderness, learn how to dance in your life, sparkling moments ... Extract Lena is fifty years old and should actually be content with Her life She has two grown-up children, a reliable husband, no problems, and she is missing the essence of life. Her husband Max gives her no endings, no caressing, no sympathy for her hormonal ups and downs. He is quite happy with the status quo and does not understand her problems at all. Coming from the older generation, where a man is the one who leaves everything, Max never knows what it is. He believes, that he has everything she needs, that he has everything for her, a house, enough money and high social status. As life goes trivialities pile up and Lena suddenly realizes, it's going to make some changes. Usually people change their spouse in that case, She loves her husband. And she is a spiritual person, who knows everything and everything in her life is a mirror. So it 's a big deal. But how life goes - she meets another man, who falls in love with her at first sight. And Lena also feels attracted to you. He is rich, he is smart, he is good-looking ... and he is honestly in love with her ... nothing lacks. Meanwhile, it is time to get back. Lena is delighted to be. Lena is delighted to be. Lena is delighted to be. Lena is delighted to be. Lena is delighted to be In contact with this old friend and soon they are so intimate with each other. Lena is chatting with her about anything, telling her about her life, her problems, her insights, her intimate things, she is talking to her. Lena is sharing so openly with her alliedly friend. It is not the only way to make a difference. Lena has feelings for the other man, too ... she is in love with two men and does not know what to do. For all of this, this is a predicament and they have to look deep in their souls to cope with all that. The essence of this book is multifaceted, but the main thing is: if you want to change something in your life, you first have to take care of yourself. If you want to know what you are doing, You can not love another person, if you do not love yourself. And as for the title - ("Because you stroke my soul" - In the end Max finds his own inner love - And out this profound and inexhaustible source he finds love in his life With love you caressed my soul.
Updates

Hello everyone, PLEASE USE THE GERMAN TITLE FOR THE COVER! Some more helpful informations: the female protagonist is not so young anymore (45) but still sexy, has long, dark hair, loves to wear shift dresses and high heels. The two male protagonists are attractive, too. Doran Pelcroft and Hollis Quarne (in the book that way) In order to have an eyecatcher and in case you choose a person for the cover - please consider that they have to attractive. I need something positive! Not dark and sinister! It's about love and light, transformation, and love of life, light, love, deep feelings, spirituality, joy, wisdom, enjoyment, tenderness, learn how to dance in your life, sparkling moments ... I have uploaded some photos - they are no must - have, i am working with pitchframe to get ideas from YOU - so, please see the photos only as an impulse. all the best! Wera Added Thursday, June 8, 2017

HI everyone, thank you all for your ideas so far, I think it is a challenge to transport the message of the book. English is not my mother tongue, so there are some misunderstandings regarding the title and the word "caressing". The dictionary gives me the translation "caressing", but it means "Touching", feeling somebody's hand on your body, saying I love you ... and: How important it is to touch somebody, to be tender ... and to touch the body, but so touching the soul. I miss a little bit the association to "caressing", (caressing / touching), to tenderness, to love. I need something to associate with my friends, being smooth, having someone who is touching your skin and enjoying that somebody is touching you. So feel free to use a body (this is a suggestion, no must have) for example ... skin ... the message how beautiful it is when somebody touches you. Touching your body ... touching your soul. Do you know what I mean?

Target Market(s)

Readers, who enjoy love-stories. Costumers who are interested in novels, entertainment, but not in cheap novelettes, women and men's customers who are interested in spiritual subjects or wisdom, quotes This book will be part of the brindle narrator prize. So it's going to be interesting for the jury. You can find the jury if you google: Larkfield Narrator Prize 2017

Requirements
Must have
• I need something positive! Not dark and sinister! It's about love and light, transformation, and love of life! - the world has a spiritual touch it is a novel after all - with all the elements a novel needs: sex, drama, love, emotions but above all: wisdom, revelations, eastern philosophies. So Iwould like to reach the mass of readers who like love stories, not only spiritual interested customers. - The cover should be an eyecatcher, even as a thumbnail, so you can play with the colors and decide for yourself to choose a monochrome design or use more colors than one.
Should not have
• Pls no sex scenes on the cover! No gloomy colors

```html
<!DOCTYPE html>
<html lang="de">
<head>
<meta charset="utf-8">
<title>Weil du meine Seele streichelst – Buchumschlag</title>
<link rel="stylesheet" href="https://fonts.googleapis.com/css2?family=Great+Vibes&family=EB+Garamond&family=Cinzel:wght@400&display=swap">
<style>
  :root {
    --wine: #3d0306;
    --wine-ink: #4e0a0d;
    --paper: #ffffff;
    --mist: #f4f5f8;
    --rock: #8a8580;
    --dress: #3a4660;
    --back-text: #f3ece8;
    --code-box: #c8c8c8;
  }
  * { margin: 0; padding: 0; box-sizing: border-box; }
  html, body {
    width: 1200px; height: 864px; overflow: hidden; background: var(--paper);
  }
  .cover {
    position: relative; width: 1200px; height: 864px; overflow: hidden;
  }
  .back-and-spine {
    position: absolute; left: 0; top: 0; width: 624px; height: 864px;
    background: var(--wine);
  }
  .blurb {
    position: absolute; left: 49px; top: 78px; width: 472px;
    font-family: "EB Garamond", serif; font-size: 16.5px; line-height: 19.2px;
    color: var(--back-text); text-align: justify; hyphens: auto;
  }
  .blurb p + p { margin-top: 19.2px; }
  .code-box {
    position: absolute; left: 366px; top: 718px; width: 155px; height: 110px;
    background: var(--code-box);
  }
  .spine-title, .spine-author {
    position: absolute; writing-mode: vertical-rl; transform: rotate(180deg);
    white-space: nowrap; color: var(--paper); font-family: "Great Vibes", cursive;
  }
  .spine-title {
    left: 580px; top: 112px; height: 372px;
    font-size: 38px; line-height: 40px; text-align: center;
  }
  .spine-author {
    left: 587px; top: 684px; height: 128px;
    font-size: 19px; line-height: 24px; font-weight: 700; text-align: center;
  }
  .front {
    position: absolute; left: 624px; top: 0; width: 576px; height: 864px; overflow: hidden;
  }
  .front-photo {
    position: absolute; inset: 0;
    background:
      radial-gradient(ellipse 60px 240px at 278px 640px, var(--dress) 0%, rgba(58,70,96,0.85) 60%, rgba(58,70,96,0) 100%),
      linear-gradient(180deg, var(--paper) 0%, var(--paper) 55%, var(--mist) 78%, #c9c4bd 88%, var(--rock) 100%);
  }
  .front-title {
    position: absolute; left: 0; top: 72px; width: 576px;
    font-family: "Great Vibes", cursive; font-weight: 400; color: var(--wine-ink);
    line-height: 108px; white-space: nowrap;
  }
  .front-title .line-one { display: block; padding-left: 20px; font-size: 108px; }
  .front-title .line-two { display: block; padding-left: 68px; font-size: 100px; }
  .front-author {
    position: absolute; left: 34px; top: 779px;
    font-family: "Cinzel", serif; color: var(--wine-ink);
    font-size: 49px; line-height: 1; white-space: nowrap;
  }
</style>
</head>
<body>
<main class="cover">
  <section class="back-and-spine">
    <div class="blurb">
      <p>Lorem ipsum dolor sit amet, consectetur adipiscing elit. Pellentesque efficitur neque et tellus cursus scelerisque. Nam ac tortor eu mauris rutrum pharetra. Cras bibendum auctor bibendum. Quisque eget sem eros. In fermentum elementum est in mattis. Curabitur dignissim feugiat odio in blandit. Pellentesque habitant morbi tristique senectus et netus et malesuada fames ac turpis egestas. Interdum et malesuada fames ac ante ipsum primis in faucibus. Proin elementum tincidunt interdum. Vestibulum ante ipsum primis in faucibus orci luctus et ultrices posuere cubilia Curae;</p>
      <p>Integer lacus arcu, tempus non commodo vestibulum, consectetur hendrerit augue. Phasellus eu massa sed lectus sodales rutrum ut ut ante. Etiam fringilla neque tellus, vel pretium risus faucibus sit amet. Sed mauris felis, imperdiet a efficitur vel, facilisis vel mi. Morbi quis quam ut tortor aliquam elementum eget eu tortor. Proin pretium nibh id vulputate ullamcorper. Ut metus urna, efficitur aliquam pulvinar at, egestas ut urna.</p>
    </div>
    <div class="code-box"></div>
    <div class="spine-title">Weil du meine Seele streichelst</div>
    <div class="spine-author">Marelka Ostrovane</div>
  </section>
  <section class="front">
    <div class="front-photo" role="img" aria-label="Photograph: a woman with long dark hair in a patterned dress seen from behind, standing on a rock ledge facing a bright misty white sea"></div>
    <h1 class="front-title">
      <span class="line-one">Weil du meine</span>
      <span class="line-two">Seele streichelst</span>
    </h1>
    <div class="front-author">Marelka Ostrovane</div>
  </section>
</main>
</body>
</html>
```